Business Card Design

We need a new buisness card designed for a new company in Darwin
We dig trenchs and lay pipes for the communication industry,Electrical industry, Teleco industry,
We also do some concrete works as well,
And small excavation work
Communication
Belvanti Contracting PTY LTD
Pit and Pipe installations
Trenching,Excavations, Concreting ,
civil works, Strutline soloutions ,over thirty years experiance
NEVER RATTLED, WE DIG AND LAY IT ALL
Contact Glen 0491536208 ps
(would like name to stand out somehow in another text or graphic sort of a way am also looking for some sort of slogan) will most likely be a red card with black writing

```html
<!DOCTYPE html>
<html lang="en">
<head>
<meta charset="utf-8">
<title>Belvanti Contracting – Business Card</title>
<link href="https://fonts.googleapis.com/css2?family=Source+Sans+3:wght@400;600&display=swap" rel="stylesheet">
<style>
  :root {
    --page-bg: #e9e6e1;
    --card-red: #d8283a;
    --card-red-deep: #b81c2c;
    --band-black: #231f20;
    --band-white: #f4f4f4;
    --machine-red: #c8202f;
    --text-white: #ffffff;
    --text-soft: #fbe9eb;
  }
  * { box-sizing: border-box; margin: 0; padding: 0; }
  html, body {
    width: 704px; height: 1200px; overflow: hidden;
    background: var(--page-bg);
    font-family: "Source Sans 3", Arial, sans-serif;
  }
  .sheet {
    width: 704px; height: 1200px;
    display: flex; flex-direction: column; justify-content: space-around; align-items: center;
    padding: 60px 0;
  }
  .card {
    position: relative;
    width: 560px; height: 320px;
    border-radius: 18px;
    overflow: hidden;
    background: linear-gradient(160deg, var(--card-red) 0%, var(--card-red-deep) 100%);
    box-shadow: 0 10px 26px rgba(0,0,0,0.22);
  }
  .band-rule {
    position: absolute; left: 0; right: 0;
    background: var(--band-black);
  }
  .card--front .band-rule { top: 218px; height: 12px; }
  .card--back .band-rule {
    top: 200px; height: 30px;
    display: flex; align-items: center; justify-content: center;
  }
  .band-machinery {
    position: absolute; left: 0; right: 0; top: 230px; bottom: 0;
    background: linear-gradient(180deg, var(--band-white) 0%, #f0d6d8 55%, var(--machine-red) 100%);
  }
  .wordmark {
    position: absolute;
    display: flex; align-items: center; gap: 14px;
    color: var(--text-white); font-weight: 400;
  }
  .wordmark__dot {
    width: 34px; height: 34px; border-radius: 50%;
    background: var(--text-white);
    flex: none;
  }
  .wordmark__name { line-height: 1.02; }
  .wordmark__name .primary { display: block; font-size: 50px; }
  .wordmark__name .secondary { display: block; font-size: 22px; }
  .card--front .wordmark { left: 90px; top: 64px; }
  .card--back .wordmark { left: 250px; top: 30px; }
  .card--back .wordmark__name .primary { font-size: 40px; }
  .card--back .wordmark__name .secondary { font-size: 18px; }
  .card--back .wordmark__dot { width: 26px; height: 26px; }
  .contact {
    position: absolute; left: 34px; top: 58px;
    color: var(--text-white); font-size: 15px; line-height: 1.25;
  }
  .contact__label { display: block; }
  .contact__person { display: block; margin-bottom: 4px; }
  .contact__name { font-weight: 600; font-size: 18px; }
  .services {
    list-style: none; color: var(--text-soft);
    font-size: 14px; line-height: 1.3;
  }
  .slogan {
    color: var(--card-red); font-size: 15px; font-weight: 600; letter-spacing: 1.5px;
    text-transform: uppercase; white-space: nowrap;
  }
</style>
</head>
<body>
<main class="sheet">
  <section class="card card--front" aria-label="Card front">
    <div class="wordmark">
      <span class="wordmark__dot"></span>
      <span class="wordmark__name">
        <span class="primary">Belvanti</span>
        <span class="secondary">Contracting PTY LTD</span>
      </span>
    </div>
    <div class="band-rule"></div>
    <div class="band-machinery" role="img" aria-label="Row of red excavator, truck and worker silhouettes on a white band"></div>
  </section>

  <section class="card card--back" aria-label="Card back">
    <div class="wordmark">
      <span class="wordmark__dot"></span>
      <span class="wordmark__name">
        <span class="primary">Belvanti</span>
        <span class="secondary">Contracting PTY LTD</span>
      </span>
    </div>
    <div class="contact">
      <span class="contact__label">Contact</span>
      <span class="contact__person"><span class="contact__name">Glen</span> 0491536208</span>
      <ul class="services">
        <li>Excavations</li>
        <li>Concreting</li>
        <li>civil works</li>
        <li>Strutline solutions</li>
        <li>Pit and Pipe installations Trenching</li>
      </ul>
    </div>
    <div class="band-rule"><p class="slogan">Never rattled, we dig and lay it all</p></div>
    <div class="band-machinery" role="img" aria-label="Row of red excavator, truck and worker silhouettes on a white band"></div>
  </section>
</main>
</body>
</html>
```